Professional digital stationary

We need a digital stationary for our brand, we already have a logo and based on that we need a design for Word, Powerpoint, mailings and Linkedin. We need to be able to re use the stationary for other things like other social media. So basically what we ask is a template for Powerpoint and Word, some e-mail headers and a nice and professional Linkedin Header.

Target Market(s)

recruitment

Font styles to use
Sans Serif

```html
<!DOCTYPE html>
<html lang="en">
<head>
<meta charset="utf-8">
<title>Brightmark – Digital Stationery</title>
<link href="https://fonts.googleapis.com/css2?family=Montserrat:wght@700&family=Open+Sans:wght@300;400;600&display=swap" rel="stylesheet">
<style>
  :root{
    --board:#a7a8ac;
    --paper:#ffffff;
    --green:#93c95a;
    --graphite:#58585a;
    --ink:#3f3f41;
    --muted:#6b6b6e;
    --photo-a:#c9cfd6;
    --photo-b:#7d8793;
    --badge-fill:#e4e7eb;
  }
  *{box-sizing:border-box;margin:0;padding:0}
  html,body{width:1200px;height:720px;overflow:hidden;background:var(--board)}
  body{position:relative;font-family:"Open Sans",Arial,sans-serif;color:var(--ink)}

  .sheet{position:absolute;background:var(--paper);overflow:hidden}
  .letter{left:40px;top:62px;width:421px;height:596px}
  .slide{width:328px;height:184px}
  .col-b{left:483px}.col-c{left:832px}
  .row-1{top:62px}.row-2{top:268px}.row-3{top:473px}

  .wordmark{position:absolute;font-family:"Open Sans",Arial,sans-serif;font-weight:300;color:var(--graphite);letter-spacing:-.02em;line-height:1}

  /* letter */
  .letter .wordmark{left:35px;top:22px;font-size:24px}
  .letter-contact{position:absolute;left:302px;top:23px;border-left:1px solid var(--green);padding-left:8px;font-size:7px;line-height:8.6px;color:var(--ink);font-style:normal}
  .contact-line{display:flex;align-items:center;gap:3px}
  .contact-line svg{width:5px;height:5px;flex:none}
  .letter-body{position:absolute;left:45px;top:143px;width:332px;font-size:6.9px;line-height:10px;color:var(--ink)}
  .letter-body p{margin-bottom:10px;text-align:justify}
  .letter-body .date{margin-bottom:10px}
  .letter-body .recipient{margin-bottom:18px;text-align:left}
  .letter-body .recipient strong{font-weight:600}
  .letter-body .salute{margin-bottom:10px}
  .signoff{position:absolute;left:45px;top:452px;font-size:6.9px}
  .signature{position:absolute;left:46px;top:462px;width:135px;height:16px;background:linear-gradient(90deg,#eeeeee,#f7f7f7)}
  .letter-band{position:absolute;left:0;bottom:0;width:421px;height:46px}

  /* slides shared */
  .slide-title{position:absolute;left:20px;top:14px;font-family:Montserrat,Arial,sans-serif;font-weight:700;font-size:8.4px;color:var(--green);letter-spacing:.01em}
  .slide .corner-mark{right:17px;top:12px;font-size:11px}
  .slide-copy{position:absolute;font-size:5.2px;line-height:7.2px;color:var(--muted);text-align:justify}
  .slide-copy p+p{margin-top:7px}
  .slide-footer{position:absolute;left:0;bottom:0;width:328px;height:22px}
  .footer-url{position:absolute;left:20px;bottom:5px;font-size:5.6px;color:#fff}

  /* cover */
  .cover .wordmark{left:17px;top:20px;font-size:21px}
  .cover-photo{position:absolute;left:0;top:0;width:328px;height:184px}
  .cover-title{position:absolute;left:17px;top:75px;font-family:Montserrat,Arial,sans-serif;font-weight:700;font-size:13.6px;color:var(--green)}
  .cover-sub{position:absolute;left:17px;top:91px;font-size:9.4px;font-weight:300;color:var(--ink)}
  .cover-url{position:absolute;left:17px;top:160px;font-size:6px;color:var(--muted)}

  /* about */
  .badge{position:absolute;left:20px;top:52px;width:80px;height:80px;border-radius:50%;background:var(--badge-fill)}
  .about-head{position:absolute;left:119px;top:51px;border-left:2px solid var(--green);padding-left:5px}
  .about-head h3{font-size:7.6px;font-weight:600;color:var(--green);line-height:9px}
  .about-head p{font-size:5.2px;color:var(--ink)}
  .about .slide-copy{left:119px;top:75px;width:192px}

  /* text slides */
  .text-only .slide-copy{left:29px;top:47px;width:270px}
  .with-photo .slide-copy{left:29px;top:49px;width:135px}
  .side-photo{position:absolute;right:0;top:0;width:200px;height:184px;background:linear-gradient(90deg,rgba(255,255,255,1) 0%,rgba(214,220,228,.7) 30%,var(--photo-a) 55%,var(--photo-b) 100%)}

  /* feature slide */
  .feature-photo{position:absolute;left:0;top:0;width:328px;height:87px;background:linear-gradient(100deg,#1d2320 0%,#3b3a44 35%,#6a5a7a 60%,#8c9a85 100%)}
  .feature .corner-mark{color:rgba(255,255,255,.55)}
  .feature-box{position:absolute;left:21px;top:35px;width:163px;height:113px;background:var(--green);padding:14px 14px}
  .feature-box .slide-copy{position:static;color:#fff}
  .partner{position:absolute;background:#77777a}
  .partner.p1{left:233px;top:111px;width:50px;height:8px;border-radius:4px}
  .partner.p2{left:220px;top:128px;width:30px;height:12px;border-radius:3px}
  .partner.p3{left:256px;top:130px;width:38px;height:7px;border-radius:2px}
  .partner.p4{left:226px;top:150px;width:14px;height:14px;border-radius:50%}
  .partner.p5{left:279px;top:150px;width:10px;height:14px}

  /* closing */
  .closing-photo{position:absolute;left:0;top:0;width:328px;height:184px}
  .closing .wordmark{left:22px;top:44px;font-size:16.5px}
  .closing-title{position:absolute;left:22px;top:93px;font-family:Montserrat,Arial,sans-serif;font-weight:700;font-size:20px;color:var(--green)}
  .closing-sub{position:absolute;left:22px;top:119px;font-size:8.6px;font-weight:300}
  .closing-contact{position:absolute;top:150px;font-size:5.8px;line-height:7.3px}
  .closing-contact.left{left:22px}
  .closing-contact.right{left:91px}
</style>
</head>
<body>

<!-- Letterhead -->
<section class="sheet letter" aria-label="Letterhead">
  <div class="wordmark">brightmark</div>
  <address class="letter-contact">
    <div>Lindenlaan 12, 4811 BK</div>
    <div>Breda</div>
    <div class="contact-line"><svg viewBox="0 0 10 10"><path d="M2 1l2 2-1 1.5c.8 1.5 1.5 2.2 3 3L7.5 6l2 2-1.5 1.5C4.5 9 1 5.5.5 2.5z" fill="var(--green)"/></svg>+31 76 55 18 240</div>
    <div class="contact-line"><svg viewBox="0 0 10 10"><rect x="0.5" y="2" width="9" height="6" fill="var(--green)"/><path d="M.5 2l4.5 3.5L9.5 2" stroke="#fff" fill="none"/></svg>info@brightmark.nl</div>
    <div class="contact-line"><svg viewBox="0 0 10 10"><circle cx="5" cy="5" r="4.5" fill="var(--green)"/><path d="M.5 5h9M5 .5c-2.5 3-2.5 6 0 9M5 .5c2.5 3 2.5 6 0 9" stroke="#fff" stroke-width=".7" fill="none"/></svg>www.brightmark.nl</div>
  </address>

  <div class="letter-body">
    <p class="date">01 January 2050</p>
    <p class="recipient"><strong>Company (Pvt) Ltd.</strong><br>PO Box 3355 Mainville St<br>Sample City Country 3355</p>
    <p class="salute">Dear Martin Verhoef,</p>
    <p>Lorem ipsum dolor sit amet, consectetuer adipiscing elit, sed diam nonummy nibh euismod tincidunt ut laoreet dolore magna aliquam erat volutpat. Ut wisi enim ad minim veniam, quis nostrud exerci tation ullamcorper suscipit lobortis nisl ut aliquip ex ea commodo consequat. Duis dolore te feugait nulla facilisi. Nam liber tempor cum soluta nobis eleifend option congue nihil imperdiet doming id quod mazim placerat facer possim assum. Lorem ipsum dolor sit amet, consectetuer adipiscing elit, sed diam nonummy nibh euismod tincidunt ut laoreet dolore magna aliquam erat volutpat. Ut wisi enim ad minim veniam, quis nostrud exerci tation ullamcorper suscipit lobortis nisl ut aliquip ex ea commodo consequat.</p>
    <p>Consectetuer adipiscing elit, sed diam nonummy nibh euismod tincidunt ut laoreet dolore magna aliquam erat volutpat. Ut wisi enim ad minim veniam, quis nostrud exerci tation ullamcorper suscipit lobortis nisl ut aliquip ex ea commodo consequat. Consectetuer adipiscing elit, sed diam nonummy nibh euismod tincidunt ut laoreet dolore magna aliquam erat volutpat. Ut wisi enim ad minim veniam, quis nostrud exerci tation ullamcorper suscipit lobortis nisl ut aliquip ex ea commodo consequat.</p>
    <p>Consectetuer adipiscing elit, sed diam nonummy nibh euismod tincidunt ut laoreet dolore magna aliquam erat volutpat. Ut wisi enim ad minim veniam, quis nostrud exerci tation ullamcorper suscipit lobortis nisl ut aliquip ex ea commodo consequat. Consectetuer adipiscing elit, sed diam nonummy nibh euismod tincidunt ut laoreet dolore magna aliquam erat volutpat. Ut wisi enim ad minim veniam, quis nostrud exerci tation ullamcorper suscipit lobortis nisl ut aliquip ex ea commodo consequat.</p>
  </div>
  <p class="signoff">Sincerely Yours</p>
  <div class="signature" role="img" aria-label="Handwritten signature of the sender"></div>

  <svg class="letter-band" viewBox="0 0 421 46" preserveAspectRatio="none" aria-hidden="true">
    <polygon points="0,38 400,0 421,0 421,1 0,44" fill="var(--green)"/>
    <polygon points="0,46 421,3 421,46" fill="var(--graphite)"/>
    <polygon points="0,41 421,1.5 421,3 0,46" fill="#fff"/>
  </svg>
</section>

<!-- Cover slide -->
<section class="sheet slide cover col-b row-1" aria-label="Presentation cover slide">
  <svg class="cover-photo" viewBox="0 0 328 184" role="img" aria-label="Photo of a recruiter working at a laptop in a bright office">
    <defs>
      <linearGradient id="coverPhoto" x1="0" y1="0" x2="1" y2="1">
        <stop offset="0" stop-color="#e3e6ea"/>
        <stop offset=".55" stop-color="#aab3bd"/>
        <stop offset="1" stop-color="#5f6874"/>
      </linearGradient>
    </defs>
    <path d="M290,0 L328,0 L328,184 L78,184 C120,160 150,150 158,128 C165,105 155,85 190,75 C225,65 240,40 255,25 C265,12 275,4 290,0Z" fill="url(#coverPhoto)"/>
    <path d="M300,0 C280,6 262,18 252,32 C240,50 222,66 192,72 C160,80 160,100 154,124 C148,146 118,160 72,184" fill="none" stroke="var(--green)" stroke-width="2.4"/>
  </svg>
  <div class="wordmark">brightmark</div>
  <h1 class="cover-title">PRESENTATION TITLE</h1>
  <p class="cover-sub">Subtitle Of The Presentation</p>
  <p class="cover-url">www.brightmark.nl</p>
</section>

<!-- About slide -->
<section class="sheet slide about col-c row-1" aria-label="About slide">
  <h2 class="slide-title">SLIDE TITLE GOES HERE</h2>
  <div class="wordmark corner-mark">brightmark</div>
  <div class="badge" role="img" aria-label="Quality certification badge"></div>
  <div class="about-head">
    <h3>About Brightmark</h3>
    <p>Brightmark is NEN-EN-ISO 9001:2015 certified</p>
  </div>
  <div class="slide-copy">
    <p>Short lines and no nonsense. The strength of Brightmark is our many years of knowledge and experience in the field. With more than 10 years of experience in IT secondment, we understand what our customers are looking for and offer suitable profiles. As a result, the search for a suitable candidate for our customers takes less time. Brightmark uses a state-of-the-art back office system, which automates a large part of the hiring process. All laws and regulations regarding the DBA Act are therefore automatically covered.</p>
  </div>
  <svg class="slide-footer" viewBox="0 0 328 22" preserveAspectRatio="none" aria-hidden="true">
    <polygon points="0,0 328,17 328,22 0,22" fill="var(--graphite)"/>
    <polygon points="0,0 328,14 328,18 0,2" fill="var(--green)"/>
  </svg>
  <span class="footer-url">www.brightmark.nl</span>
</section>

<!-- Text slide -->
<section class="sheet slide text-only col-b row-2" aria-label="Text slide">
  <h2 class="slide-title">SLIDE TITLE GOES HERE</h2>
  <div class="wordmark corner-mark">brightmark</div>
  <div class="slide-copy">
    <p>Lorem Ipsum is simply dummy text of the printing and typesetting industry. Lorem Ipsum has been the industry's standard dummy text ever since the 1500s, when an unknown printer took a galley of type and scrambled it to make a type specimen book. It has survived not only five centuries, but also the leap into electronic typesetting, remaining essentially unchanged. It was popularised in the 1960s with the release of transfer sheets containing Lorem Ipsum passages, and more recently with desktop publishing software and layout programs including versions of Lorem Ipsum.</p>
    <p>It is a long established fact that a reader will be distracted by the readable content of a page when looking at its layout. The point of using Lorem Ipsum is that it has a more-or-less normal distribution of letters, as opposed to using 'Content here, content here', making it look like readable English. Many desktop publishing packages and web page editors now use Lorem Ipsum as their default model text, and a search for 'lorem ipsum' will uncover many web sites still in their infancy. Various versions have evolved over the years, sometimes by accident, sometimes on purpose (injected humour and the like).</p>
  </div>
  <svg class="slide-footer" viewBox="0 0 328 22" preserveAspectRatio="none" aria-hidden="true">
    <polygon points="0,0 328,17 328,22 0,22" fill="var(--graphite)"/>
    <polygon points="0,0 328,14 328,18 0,2" fill="var(--green)"/>
  </svg>
  <span class="footer-url">www.brightmark.nl</span>
</section>

<!-- Text with photo slide -->
<section class="sheet slide with-photo col-c row-2" aria-label="Text and photo slide">
  <div class="side-photo" role="img" aria-label="Photo of a smiling consultant in a suit at a meeting table with charts"></div>
  <h2 class="slide-title">SLIDE TITLE GOES HERE</h2>
  <div class="wordmark corner-mark">brightmark</div>
  <div class="slide-copy">
    <p>Lorem Ipsum is simply dummy text of the printing and typesetting industry. Lorem Ipsum has been the industry's standard dummy text ever since the 1500s, when an unknown printer took a galley of type and scrambled it to make a type specimen book. It has survived not only five centuries, but also the leap into electronic typesetting, remaining essentially unchanged. It was popularised in the 1960s with the release of transfer sheets containing Lorem Ipsum passages, and more recently with desktop publishing software and layout programs including versions of Lorem Ipsum.</p>
  </div>
  <svg class="slide-footer" viewBox="0 0 328 22" preserveAspectRatio="none" aria-hidden="true">
    <polygon points="0,0 328,17 328,22 0,22" fill="var(--graphite)"/>
    <polygon points="0,0 328,14 328,18 0,2" fill="var(--green)"/>
  </svg>
  <span class="footer-url">www.brightmark.nl</span>
</section>

<!-- Feature slide -->
<section class="sheet slide feature col-b row-3" aria-label="Feature slide with clients">
  <div class="feature-photo" role="img" aria-label="Photo of a row of office monitors and chairs"></div>
  <h2 class="slide-title">SLIDE TITLE GOES HERE</h2>
  <div class="wordmark corner-mark">brightmark</div>
  <div class="feature-box">
    <p class="slide-copy">Lorem Ipsum is simply dummy text of the printing and typesetting industry. Lorem Ipsum has been the industry's standard dummy text ever since the 1500s, when an unknown printer took a galley of type and scrambled it to make a type specimen book. It has survived not only five centuries, but also the leap into electronic typesetting, remaining essentially unchanged. It was popularised in the 1960s with the release of transfer sheets containing Lorem Ipsum passages, and more recently with desktop publishing software and layout programs including versions of Lorem Ipsum.</p>
  </div>
  <div class="partner p1" role="img" aria-label="Client logo"></div>
  <div class="partner p2" role="img" aria-label="Client logo"></div>
  <div class="partner p3" role="img" aria-label="Client logo"></div>
  <div class="partner p4" role="img" aria-label="Client logo"></div>
  <div class="partner p5" role="img" aria-label="Client logo"></div>
</section>

<!-- Closing slide -->
<section class="sheet slide closing col-c row-3" aria-label="Closing slide">
  <svg class="closing-photo" viewBox="0 0 328 184" role="img" aria-label="Photo of colleagues reviewing charts and documents at a desk">
    <defs>
      <linearGradient id="closingPhoto" x1="0" y1="0" x2="1" y2="1">
        <stop offset="0" stop-color="#e8ebee"/>
        <stop offset=".5" stop-color="#b6bec7"/>
        <stop offset="1" stop-color="#4f5863"/>
      </linearGradient>
    </defs>
    <path d="M36,0 L328,0 L328,184 L232,184 C205,165 212,135 195,112 C178,92 140,100 125,82 C112,65 118,40 100,28 C85,18 60,20 36,0Z" fill="url(#closingPhoto)"/>
  </svg>
  <div class="wordmark">brightmark</div>
  <h2 class="closing-title">Thank You!</h2>
  <p class="closing-sub">Stay In Touch With Us...</p>
  <div class="closing-contact left">
    <div class="contact-line"><svg viewBox="0 0 10 10"><path d="M2 1l2 2-1 1.5c.8 1.5 1.5 2.2 3 3L7.5 6l2 2-1.5 1.5C4.5 9 1 5.5.5 2.5z" fill="var(--green)"/></svg>+31 76 55 18 240</div>
    <div class="contact-line"><svg viewBox="0 0 10 10"><rect x="0.5" y="2" width="9" height="6" fill="var(--green)"/><path d="M.5 2l4.5 3.5L9.5 2" stroke="#fff" fill="none"/></svg>info@brightmark.nl</div>
    <div class="contact-line"><svg viewBox="0 0 10 10"><circle cx="5" cy="5" r="4.5" fill="var(--green)"/><path d="M.5 5h9M5 .5c-2.5 3-2.5 6 0 9M5 .5c2.5 3 2.5 6 0 9" stroke="#fff" stroke-width=".7" fill="none"/></svg>www.brightmark.nl</div>
  </div>
  <div class="closing-contact right">
    <div>Brightmark</div>
    <div>Lindenlaan 12, 4811 BK</div>
    <div>Breda</div>
  </div>
</section>

</body>
</html>
```